BRONT (Bright Routing Online Network Tools) Letter Head Design Project

Company Name: BRONT (Bright Routing Online Network Tools) JLT.
Office Address: Office No 718, Saffron Crest Building, Marwah Garden Quarter, Dubai, U.A.E
Company line of business:
1) Currently we have a POS solution for retail outlets like duty free shops, supermarkets, department stores etc... The solution is deployed in Palmgate Travel Retail on 350 POS and in Corniche Transit Stores on 100 POS. So our main line of business is the deployment of this solution in retail outlets locally or regionally. We have already deployed the solution in India and Australia.
2) Integration of other third party POS systems with an online credit authorization netwotk in the UAE. This will enable POS applications to connect directly to the acquiring banks without needing an EFT terminal like Paxolan or Trenvira. The credit card payment is completed at the POS.
3) Other solutions that are targeting retail outlets like mobile POS, queue busting solutions, stock taking solutions using hand held devices, transaction capture systems, etc...
4) Other IT services like support of call center solutions from Orbisan Callworks and development of new solutions as per customer requirements.
We need a letter head design for the company. We don't have any specific requirements in mind and we prefer to leave it up to the designers to come up with creative designs that will not be limited by any guidelines.
Updates
I have just uploaded all the files I received from my company logo designer. Please review and let me know if you need anything else. .
Dear All,
I have received very nice designs and I thank you for all the hard work you have put so far. I would like the letter head to have all the following company details:
Office Address: Office No 718, Saffron Crest Building, MGQ, Dubai UAE
P.O.Box: 58316 Dubai UAE
Tel Number:+971-4-5817260
Fax Number::+971-4-5817261
Website:www.brontmgq.example
I would also like to represent the company details as a QRCode somewhere on the page, probably next to the company details if possible (as a trial).
In case you have included a butterfly in the middle of the page as part of your design, I prefer that it doesn't include any colors as colors might make reading the text on the page more difficult.
I don't want to have too many butterflies on the page. 2 are more than enough.
Can you also include a design for the continuation pages?
Thank you in advance and I look forward to receiving your creative designs.
Regards
Samir Toufany

```html
<!DOCTYPE html>
<html lang="en">
<head>
<meta charset="utf-8">
<title>BRONT Letterhead</title>
<link rel="stylesheet" href="https://fonts.googleapis.com/css2?family=Open+Sans:wght@400;600&family=Carlito&display=swap">
<style>
  :root {
    --brand: #ef6c50;
    --tagline: #7a7a7a;
    --watermark: #f3f3f3;
    --paper: #ffffff;
    --on-brand: #ffffff;
  }
  html, body {
    margin: 0;
    padding: 0;
    overflow: hidden;
    background: var(--paper);
  }
  .letterhead {
    position: relative;
    width: 848px;
    height: 1200px;
    overflow: hidden;
    background: var(--paper);
    font-family: "Open Sans", sans-serif;
  }
  .brand-mark {
    position: absolute;
    left: 12px;
    top: 14px;
    width: 26px;
    height: 26px;
    border-radius: 50%;
    background: var(--brand);
  }
  .brand-name {
    position: absolute;
    left: 46px;
    top: 82px;
    transform: translateY(-100%);
    font-family: "Open Sans", sans-serif;
    font-weight: 600;
    font-size: 70px;
    line-height: 0.74;
    color: var(--brand);
    white-space: nowrap;
  }
  .brand-tagline {
    position: absolute;
    left: 296px;
    top: 64px;
    font-family: "Open Sans", sans-serif;
    font-weight: 400;
    font-size: 19px;
    line-height: 22px;
    color: var(--tagline);
    white-space: nowrap;
  }
  .header-rule {
    position: absolute;
    left: 8px;
    top: 98px;
    width: 832px;
    height: 2px;
    background: var(--brand);
  }
  .watermark {
    position: absolute;
    left: 0;
    top: 498px;
    width: 848px;
    text-align center;
    text-align: center;
    font-family: "Open Sans", sans-serif;
    font-weight: 600;
    font-size: 190px;
    line-height: 1;
    color: var(--watermark);
    user-select: none;
  }
  .skyline-band {
    position: absolute;
    left: 0;
    top: 1094px;
    width: 848px;
    height: 102px;
    background: var(--brand);
  }
  .footer-address {
    position: absolute;
    left: 664px;
    top: 1112px;
    margin: 0;
    font-family: "Carlito", sans-serif;
    font-style: normal;
    font-size: 11.5px;
    line-height: 16.3px;
    color: var(--on-brand);
    white-space: nowrap;
  }
</style>
</head>
<body>
  <main class="letterhead">
    <header>
      <span class="brand-mark"></span>
      <span class="brand-name">BRONT</span>
      <span class="brand-tagline">Bright Routing Online Network Tools</span>
    </header>
    <div class="header-rule"></div>

    <div class="watermark" aria-hidden="true">BRONT</div>

    <div class="skyline-band" role="img" aria-label="City skyline silhouette in brand orange along the foot of the page"></div>

    <address class="footer-address">
      Bright Routing Online Network Tools<br>
      Office No 718,<br>
      Saffron Crest Building,<br>
      Marwah Garden Quarter,<br>
      Dubai, U.A.E
    </address>
  </main>
</body>
</html>
```